Business Card Design For A Renovation Contractor Company

We need a business card for a new company based in Singapore, our company name is "KT Planora". We are a renovation contractor that builds designs into reality. We build more of F&B restaurants, retail stores and commercial offices. We work very closely with designers. The final design should communicate to our client that we are a company that you can trust, that will plan and complete your project without giving you a headache. I like my client to remember my company as "KT". The beauty of SIMPLE is important.

Industry/Entity Type

Contractor

Requirements
Nice to have
• Black or Red base

```html
<!DOCTYPE html>
<html lang="en">
<head>
<meta charset="utf-8">
<title>KT Planora – Business Card</title>
<link href="https://fonts.googleapis.com/css2?family=Questrial&family=Open+Sans:wght@400;700&display=swap" rel="stylesheet">
<style>
  :root {
    --backdrop: #d9d6d2;
    --card-black: #0b0b0b;
    --card-white: #ffffff;
    --brand-red: #e0141b;
    --ink: #111111;
    --muted: #6b6b6b;
    --faint-ring: #3a3a3a;
    --divider: #e4e4e4;
  }
  * { margin: 0; padding: 0; box-sizing: border-box; }
  html, body { width: 1200px; height: 900px; overflow: hidden; }
  body { background: var(--backdrop); position: relative; font-family: "Open Sans", sans-serif; }

  .card { position: absolute; left: 250px; width: 700px; height: 400px; box-shadow: 0 8px 24px rgba(0,0,0,.22); overflow: hidden; }

  /* Back side */
  .card-back { top: 35px; background: var(--card-black); }
  .card-back .ring { position: absolute; left: 30px; top: 40px; width: 340px; height: 340px; border-radius: 50%; border: 24px solid var(--faint-ring); }
  .card-back .brand { position: absolute; right: 40px; top: 150px; text-align: right; }
  .brand-name { font-family: "Questrial", sans-serif; font-size: 50px; line-height: 1; letter-spacing: -1px; white-space: nowrap; }
  .card-back .brand-name { color: var(--card-white); }
  .tagline { font-family: "Questrial", sans-serif; font-size: 18px; letter-spacing: .3px; margin-top: 6px; white-space: nowrap; }
  .card-back .tagline { color: var(--card-white); }

  /* Front side */
  .card-front { top: 465px; background: var(--card-white); display: flex; }
  .front-brand { width: 44%; display: flex; flex-direction: column; justify-content: center; align-items: center; border-right: 1px solid var(--divider); box-shadow: 6px 0 10px -8px rgba(0,0,0,.25); padding-top: 40px; }
  .front-brand .mark { width: 58px; height: 58px; border-radius: 50%; border: 6px solid var(--brand-red); margin-bottom: 14px; }
  .front-brand .brand-name { color: var(--ink); font-size: 40px; }
  .front-brand .tagline { color: var(--ink); font-size: 15px; }

  .front-details { flex: 1; padding: 46px 0 0 56px; color: var(--muted); font-size: 15px; }
  .person-name { color: var(--brand-red); font-weight: 700; font-size: 20px; }
  .person-role { font-size: 13px; margin-bottom: 34px; }
  .address { font-style: normal; line-height: 1.4; margin-bottom: 22px; }
  .contact-list { list-style: none; line-height: 1.55; }
  .contact-list li { display: flex; align-items: center; gap: 10px; }
  .contact-list svg { width: 14px; height: 14px; fill: none; stroke: var(--brand-red); stroke-width: 2; }
</style>
</head>
<body>

<section class="card card-back" aria-label="Card back">
  <div class="ring"></div>
  <div class="brand">
    <div class="brand-name">KT Planora</div>
    <div class="tagline">turning plans into spaces</div>
  </div>
</section>

<section class="card card-front" aria-label="Card front">
  <div class="front-brand">
    <div class="mark"></div>
    <div class="brand-name">KT Planora</div>
    <div class="tagline">turning plans into spaces</div>
  </div>
  <div class="front-details">
    <div class="person-name">Marcus Tan</div>
    <div class="person-role">Director</div>
    <address class="address">
      Aldren Road #07-2204<br>
      Aldren Complex<br>
      Singapore 418562
    </address>
    <ul class="contact-list">
      <li><svg viewBox="0 0 16 16"><path d="M3 2h3l1 4-2 1a8 8 0 0 0 4 4l1-2 4 1v3a1 1 0 0 1-1 1A12 12 0 0 1 2 3a1 1 0 0 1 1-1z"/></svg>341 555 0170 0</li>
      <li><svg viewBox="0 0 16 16"><rect x="2" y="6" width="12" height="6"/><rect x="4" y="2" width="8" height="4"/><rect x="4" y="10" width="8" height="4"/></svg>341 555 0170 7</li>
      <li><svg viewBox="0 0 16 16"><rect x="1.5" y="3.5" width="13" height="9"/><path d="M1.5 3.5 8 9l6.5-5.5"/></svg>marcus@ktplanora.com</li>
      <li><svg viewBox="0 0 16 16"><circle cx="8" cy="8" r="6.5"/><path d="M1.5 8h13M8 1.5c3 3 3 10 0 13M8 1.5c-3 3-3 10 0 13"/></svg>www.ktplanora.com</li>
    </ul>
  </div>
</section>

</body>
</html>
```